Letterhead for Dane Holloway

I need a letterhead based on the business card design

Industry/Entity Type

Business

Requirements
Must have
• Footer: Dane Holloway Naturopath
Shop 3042c, 451 Marrow Lane, Sydney 2000

```html
<!DOCTYPE html>
<html lang="en">
<head>
<meta charset="utf-8">
<title>Dane Holloway Naturopath – Letterhead</title>
<link href="https://fonts.googleapis.com/css2?family=Open+Sans:wght@400;600&family=Great+Vibes&display=swap" rel="stylesheet">
<style>
  :root {
    --backdrop: #7d8a90;
    --paper: #f4f4f2;
    --ink: #2b2b2b;
    --accent: #e07f1f;
    --leaf-light: #f2b577;
    --leaf-deep: #e38e3c;
  }
  html, body {
    margin: 0;
    padding: 0;
    width: 1200px;
    height: 795px;
    overflow: hidden;
    background: var(--backdrop);
  }
  .letterhead {
    position: absolute;
    left: 333px;
    top: 20px;
    width: 534px;
    height: 755px;
    background: var(--paper);
    overflow: hidden;
    font-family: "Open Sans", Arial, sans-serif;
    color: var(--ink);
  }
  .brand {
    position: absolute;
    left: 40px;
    top: 48px;
    display: flex;
    align-items: center;
    gap: 8px;
  }
  .brand-dot {
    width: 12px;
    height: 12px;
    border-radius: 50%;
    background: var(--accent);
  }
  .brand-name {
    font-size: 15px;
    font-weight: 600;
    letter-spacing: 0.12em;
    text-transform: uppercase;
    color: var(--accent);
    line-height: 1.25;
  }
  .leaf-art {
    position: absolute;
    left: -10px;
    bottom: 30px;
    width: 360px;
    height: 360px;
  }
  .letter-body {
    position: absolute;
    left: 78px;
    top: 132px;
    width: 400px;
    font-size: 9.2px;
    line-height: 1.62;
  }
  .letter-body p {
    margin: 0 0 22px;
  }
  .sign-off {
    position: absolute;
    left: 220px;
    top: 470px;
    font-family: "Great Vibes", cursive;
    color: var(--ink);
  }
  .sign-off .closing {
    font-size: 24px;
    display: block;
  }
  .sign-off .signature {
    font-size: 26px;
    display: block;
    margin: 4px 0 0 30px;
  }
  .footer {
    position: absolute;
    left: 40px;
    right: 40px;
    bottom: 22px;
    display: flex;
    justify-content: space-between;
    font-size: 8.5px;
    font-weight: 600;
    color: var(--accent);
  }
</style>
</head>
<body>
  <main class="letterhead">
    <header class="brand">
      <span class="brand-dot"></span>
      <span class="brand-name">Dane Holloway Naturopathy</span>
    </header>

    <svg class="leaf-art" viewBox="0 0 360 360" role="img" aria-label="Cluster of large overlapping orange leaves illustration">
      <defs>
        <linearGradient id="leafFill" x1="0" y1="0" x2="1" y2="1">
          <stop offset="0" stop-color="var(--leaf-light)"/>
          <stop offset="1" stop-color="var(--leaf-deep)"/>
        </linearGradient>
      </defs>
      <path d="M0 20 C90 40 200 120 300 200 C350 240 360 300 340 350 L0 360 Z" fill="url(#leafFill)" opacity="0.85"/>
    </svg>

    <section class="letter-body">
      <p>Lorem ipsum dolor sit amet, consectetur adipiscing elit. Maecenas lobortis sodales consectetur. Maecenas gravida accumsan nulla, vitae sollicitudin orci sodales vel. Nunc sit amet sapien quis nulla dictum varius eu et metus. Sed lacus turpis, vehicula quis velit quis, luctus dignissim justo. Ut gravida, velit eu pretium commodo, ante purus fermentum leo, vitae iaculis lorem massa sit amet purus. Nam posuere pretium cursus. Nunc condimentum auctor nibh, ac ullamcorper massa congue nec. Vestibulum scelerisque nisi mauris. Ut in magna nunc. Duis sodales cursus vehicula. Cras augue odio, ullamcorper id commodo vel, pellentesque eget erat. Proin condimentum diam a consectetur semper. Aenean vitae faucibus nisi. Phasellus venenatis turpis orci. Curabitur pharetra nunc ac mauris rhoncus facilisis. Ut vestibulum, risus non hendrerit scelerisque, est felis dignissim quam, vitae vehicula lacus nisl id urna.</p>
      <p>Donec condimentum pulvinar nisl quis eleifend. Mauris volutpat aliquet lobortis. Suspendisse potenti. Nullam sed suscipit erat, ut auctor mauris. Nulla et felis at ipsum tincidunt convallis nec sit amet nisl. Nulla facilisi. Nam a tellus mi. Phasellus venenatis lacinia massa. Nulla ut felis ipsum. Class aptent taciti sociosqu ad litora torquent per conubia nostra, per inceptos himenaeos. Vestibulum imperdiet eros urna, id viverra mauris blandit a. Maecenas laoreet, massa quis laoreet ultrices, leo augue mollis metus, ac vestibulum risus lectus a dui. Mauris blandit sapien vitae felis malesuada hendrerit.</p>
    </section>

    <div class="sign-off">
      <span class="closing">Sincerly</span>
      <span class="signature">Dane Holloway</span>
    </div>

    <footer class="footer">
      <span class="footer-web">daneholloway.com.au</span>
      <span class="footer-email">dhnaturopath@leafpost.com.au</span>
      <span class="footer-address">Shop 3042c, 451 Marrow Lane, Sydney 2000</span>
    </footer>
  </main>
</body>
</html>
```